I need a Kestrels-themed graphic made in the style of the two of deon farrowby i have attached

I need a social media graphic made for the Kestrels in the style of the two of Deon Farrowby I have attached

Words wise i need

"Good luck, Bartley" (this should be most prominent)
"in your first Kestrels Appearance"

then somewhere put "Thank you for making the Pallix Tour part of your journey to golf's grand stage. This is your moment and we'll proudly be cheering you on."

Maybe use the photo of him fist pumping and cut him out to be the centerpiece and use some of the old photos around it. Not all the photos have to be used, but make sure to get the one of him wearing the green jacket. I need this by wednesday afternoon so I will pick a winner soon!

```html
<!DOCTYPE html>
<html lang="en">
<head>
<meta charset="utf-8">
<title>Good Luck, Bartley</title>
<link rel="stylesheet" href="https://fonts.googleapis.com/css2?family=Archivo:wght@700;800;900&family=Source+Sans+3:wght@400;500&display=swap">
<style>
  :root {
    --canvas: #ffffff;
    --paper: #efe3c8;
    --paper-dark: #e2d2ad;
    --green: #2f5a3c;
    --green-deep: #1f4129;
    --green-soft: #4d7a52;
    --gold: #c9a35c;
    --gold-light: #e0c487;
    --gold-dark: #a98540;
    --cream-text: #f1e6cc;
    --ink: #2a2a24;
    --frame: #f3ecdc;
    --tape: rgba(222, 205, 160, 0.85);
  }
  * { box-sizing: border-box; margin: 0; padding: 0; }
  html, body { width: 1200px; height: 1200px; overflow: hidden; background: var(--canvas); }
  .canvas { position: relative; width: 1200px; height: 1200px; background: var(--canvas); }

  .banner {
    position: absolute; left: 35px; top: 362px; width: 1137px; height: 482px;
    background: linear-gradient(135deg, var(--paper) 0%, var(--paper-dark) 50%, var(--paper) 100%);
  }
  .panel {
    position: absolute; left: 17px; top: 13px; width: 1104px; height: 456px;
    background: radial-gradient(ellipse at 50% 35%, var(--green-soft) 0%, var(--green) 45%, var(--green-deep) 100%);
    overflow: hidden;
  }
  .panel-rule {
    position: absolute; left: 7px; top: 6px; right: 7px; bottom: 6px;
    border: 1.5px solid var(--gold); pointer-events: none; z-index: 6;
  }
  .scene { position: absolute; }
  .scene-left {
    left: 0; top: 90px; width: 420px; height: 366px;
    background:
      radial-gradient(ellipse at 25% 80%, rgba(214, 104, 150, 0.85) 0%, rgba(190, 90, 130, 0.5) 35%, rgba(47, 90, 60, 0) 70%),
      linear-gradient(90deg, rgba(200, 205, 200, 0.3) 0%, rgba(47, 90, 60, 0) 85%);
  }
  .scene-right {
    right: 0; top: 90px; width: 320px; height: 366px;
    background:
      linear-gradient(180deg, rgba(60, 95, 60, 0.15) 0%, rgba(95, 140, 80, 0.5) 55%, rgba(200, 195, 180, 0.4) 72%, rgba(70, 120, 65, 0.55) 100%);
  }

  .badge { position: absolute; left: 539px; top: 0; width: 61px; height: 64px; z-index: 8; }
  .badge-shape { position: absolute; left: 0; top: 0; width: 61px; height: 64px; }
  .badge-name {
    position: absolute; left: 0; top: 24px; width: 61px; text-align: center;
    font-family: "Archivo", sans-serif; font-weight: 800; font-size: 10.5px; color: var(--green-deep);
  }

  .headline {
    position: absolute; left: 0; width: 100%; top: 50px; text-align: center; z-index: 4;
    font-family: "Archivo", sans-serif; font-weight: 900; font-size: 71px; line-height: 1;
    letter-spacing: 0.5px; text-transform: uppercase;
    background: linear-gradient(180deg, var(--gold-light) 0%, var(--gold) 55%, var(--gold-dark) 100%);
    -webkit-background-clip: text; background-clip: text; color: transparent;
    filter: drop-shadow(0 3px 3px rgba(0, 0, 0, 0.45));
  }
  .subhead {
    position: absolute; left: 0; width: 100%; top: 120px; text-align: center; z-index: 7;
    font-family: "Archivo", sans-serif; font-weight: 800; font-size: 27px; line-height: 1;
    color: var(--cream-text); text-transform: uppercase; letter-spacing: 0.3px;
    text-shadow: 0 2px 3px rgba(0, 0, 0, 0.4);
  }

  .photo {
    position: absolute; border: 5px solid var(--frame);
    box-shadow: 0 3px 8px rgba(0, 0, 0, 0.4); z-index: 3;
  }
  .tape {
    position: absolute; top: -9px; left: 50%; width: 62px; height: 14px; margin-left: -31px;
    background: var(--tape);
  }
  .photo-trophy { left: 134px; top: 167px; width: 202px; height: 152px;
    background: linear-gradient(135deg, #8a7258 0%, #b9b2a6 40%, #6b7c93 70%, #d9d4cc 100%); }
  .photo-swing { left: 317px; top: 198px; width: 140px; height: 152px;
    background: linear-gradient(180deg, #9fb8cf 0%, #7d9a68 45%, #5f7f45 80%, #3c6e4e 100%); }
  .photo-scorecard { left: 684px; top: 198px; width: 139px; height: 154px;
    background: linear-gradient(180deg, #8fa8c6 0%, #6c8d55 35%, #d98a6a 65%, #e8e6e0 100%); }
  .photo-green { left: 812px; top: 180px; width: 200px; height: 140px;
    background: linear-gradient(180deg, #6f8860 0%, #4a5e52 40%, #5f9a4b 70%, #7db463 100%); }

  .cutout {
    position: absolute; left: 425px; top: 160px; width: 258px; height: 296px; z-index: 3;
    background: linear-gradient(160deg, #a98a6a 0%, #d8cdb8 35%, #f0ece2 60%, #e6e0d2 100%);
    border-radius: 48% 48% 0 0 / 28% 28% 0 0;
    box-shadow: 0 0 0 4px var(--paper);
  }

  .message {
    position: absolute; left: 235px; top: 369px; width: 634px; height: 52px; z-index: 5;
    background: var(--paper); border: 2px solid var(--gold);
    box-shadow: 0 2px 6px rgba(0, 0, 0, 0.35);
    display: flex; align-items: center; justify-content: center; text-align: center;
    font-family: "Source Sans 3", sans-serif; font-weight: 400; font-size: 16.5px; line-height: 1.15;
    color: var(--ink);
  }
  .club-name {
    position: absolute; left: 696px; top: 426px; z-index: 5;
    font-family: "Source Sans 3", sans-serif; font-weight: 500; font-size: 11px; letter-spacing: 0.4px;
    color: var(--gold-light); text-transform: uppercase; white-space: nowrap;
  }
</style>
</head>
<body>
<div class="canvas">
  <div class="banner">
    <div class="panel">
      <div class="scene scene-left" role="img" aria-label="Flowering pink azaleas in front of a white clubhouse"></div>
      <div class="scene scene-right" role="img" aria-label="Tall pines above a putting green and bunker"></div>

      <h1 class="headline">Good Luck, Bartley</h1>
      <p class="subhead">In Your First Kestrels Appearance</p>

      <div class="photo photo-trophy" role="img" aria-label="Bartley holding a championship trophy with two others"><span class="tape"></span></div>
      <div class="photo photo-swing" role="img" aria-label="Young Bartley swinging a club on the range"><span class="tape"></span></div>
      <div class="cutout" role="img" aria-label="Bartley embracing his mother after qualifying"></div>
      <div class="photo photo-scorecard" role="img" aria-label="Young Bartley holding up a scorecard"><span class="tape"></span></div>
      <div class="photo photo-green" role="img" aria-label="Bartley celebrating on the green before a crowd"><span class="tape"></span></div>

      <div class="message">Thank you for making the Pallix Tour part of your journey to golf's grand stage.<br>This is your moment and we'll proudly be cheering you on.</div>
      <p class="club-name">Brindlewood National Golf Club</p>

      <div class="panel-rule"></div>
    </div>

    <div class="badge">
      <svg class="badge-shape" viewBox="0 0 61 64" aria-hidden="true">
        <polygon points="0,0 61,0 61,52 30.5,64 0,52" fill="#efe3c8" stroke="#c9a35c" stroke-width="1.5"/>
      </svg>
      <span class="badge-name">Kestrels</span>
    </div>
  </div>
</div>
</body>
</html>
```